Simple, High-Class Web Design Wanted - Motivational Speakers Site

1. Full Brief/Request & Specs outlined on following video -
http://clipvane-recorder.com/watch/tbWrkLmQyP

2. Use colours, images as you feel suits objective (we are happy to pay up to US$30 for any good images but must have licence/permission).

3. Layout probably similar to existing site - www.podiumvoicehub.com.au / http://podiumvoicehub.com.au/contact.php

4. Must Be Able to Coded for MOBILE-FRIENDLINESS & WordPress friendly Ideal.

5. This is the first, small job of many we/graphic design jobs. If suits, winning designer may be offered all future work direct.

Thanks & look forward to your design. Glen.

Target Market(s)

corporates - high end

Number of Pages Required

2 page

Font styles to use
Sans Serif

Requirements
Must have
• Classy professional look
Nice to have
• all in Video in brief
Should not have
• too many images / new images I haven't approved

```html
<!DOCTYPE html>
<html lang="en">
<head>
<meta charset="utf-8">
<title>Podium Voice Hub</title>
<link href="https://fonts.googleapis.com/css2?family=Open+Sans:wght@400;600;700;800&display=swap" rel="stylesheet">
<style>
:root{
  --orange:#f39019;
  --orange-deep:#e67e0e;
  --ink:#333333;
  --muted:#6b6b6b;
  --dark:#2b2b2b;
  --white:#ffffff;
  --line:#e2e2e2;
}
*{box-sizing:border-box;margin:0;padding:0}
html,body{width:724px;height:1200px;overflow:hidden;background:var(--white)}
body{font-family:"Open Sans",Arial,sans-serif;color:var(--ink);font-size:8px;line-height:1.45}
.page{width:724px;height:1200px;position:relative;overflow:hidden}

/* header */
.topbar{height:40px;display:flex;align-items:center;justify-content:space-between;padding:0 30px}
.brand{font-size:20px;font-weight:700;color:var(--orange);letter-spacing:-.2px}
.top-icons{display:flex;gap:6px}
.top-icons span{width:14px;height:14px;border-radius:50%;background:#bdbdbd;display:block}
.nav{height:18px;background:var(--orange);display:flex;align-items:center;padding:0 30px;gap:14px}
.nav a{color:var(--white);font-size:7px;font-weight:700;text-decoration:none;letter-spacing:.3px}

/* hero */
.hero{height:312px;position:relative;background:linear-gradient(180deg,#6d7e8c 0%,#4f5a63 35%,#3b3a38 70%,#2a2622 100%)}
.hero-photo{position:absolute;inset:0}
.hero-copy{position:absolute;left:0;right:0;top:104px;text-align:center}
.hero-title{font-size:31px;font-weight:700;color:var(--white);letter-spacing:.5px}
.hero-sub{font-size:13px;color:var(--orange);font-weight:600;margin-top:-2px}
.btn{display:inline-block;font-weight:700;text-decoration:none}
.btn-orange{background:var(--orange);color:var(--white)}
.hero .btn{margin-top:16px;font-size:7px;padding:7px 14px;border-radius:2px}
.arrow{position:absolute;top:148px;width:22px;height:22px;border-radius:50%;background:var(--orange);display:flex;align-items:center;justify-content:center}
.arrow.left{left:18px}.arrow.right{right:18px}
.dots{position:absolute;right:22px;top:178px;display:flex;flex-direction:column;gap:6px}
.dots span{width:7px;height:7px;border-radius:50%;background:rgba(255,255,255,.55)}
.dots span:first-child{background:var(--white)}

/* welcome */
.welcome{height:190px;background:linear-gradient(180deg,var(--orange) 0%,var(--orange-deep) 100%);text-align:center;padding:38px 120px 0;color:var(--white)}
.welcome h2{font-size:21px;font-weight:700}
.welcome-rule{width:40px;height:2px;background:var(--white);margin:6px auto 10px}
.welcome p{font-size:6.5px;line-height:1.6;opacity:.95}
.btn-white{background:var(--white);color:var(--orange);font-size:7.5px;padding:7px 22px;border-radius:14px;margin-top:16px}

/* intro */
.intro{height:262px;display:flex;padding:26px 30px 0 40px;gap:22px}
.video{width:290px;flex:none}
.video-frame{width:290px;height:180px;background:linear-gradient(160deg,#e9e4df 0%,#c9c3bd 55%,#8a8580 100%);position:relative;display:flex;flex-direction:column;align-items:center;justify-content:center}
.play{width:36px;height:36px;border-radius:50%;background:rgba(0,0,0,.45);display:flex;align-items:center;justify-content:center}
.video-label{color:var(--white);font-size:10px;font-weight:600;margin-top:8px;text-shadow:0 1px 2px rgba(0,0,0,.5)}
.video .btn{margin-top:10px;margin-left:2px;font-size:7.5px;padding:7px 12px;border-radius:2px}
.pitch h3{font-size:13px;font-weight:700;line-height:1.25;color:var(--dark)}
.pitch h3 .accent{color:var(--orange)}
.pitch p{font-size:6.2px;color:var(--muted);margin-top:8px;line-height:1.55}
.ticks{list-style:none;margin-top:6px}
.ticks li{font-size:6.2px;color:var(--muted);display:flex;gap:5px;align-items:center;line-height:1.7}

/* note */
.note{height:138px;background:linear-gradient(180deg,#3a3a3a 0%,#262626 100%);padding:20px 70px 0;color:var(--white)}
.note h4{font-size:15px;font-weight:700;text-align:center;margin-bottom:10px}
.note ul{list-style:none}
.note li{font-size:6.5px;line-height:1.5;display:flex;gap:6px;margin-bottom:4px;opacity:.92}
.note li::before{content:"";width:5px;height:5px;border-radius:50%;background:var(--white);flex:none;margin-top:3px}

/* footer */
.footer{height:200px;display:grid;grid-template-columns:1fr 1fr 1fr 1fr;gap:18px;padding:22px 30px 0}
.footer h5{font-size:11px;font-weight:700;color:var(--dark);margin-bottom:8px}
.footer h5.brand-foot{color:var(--orange)}
.footer p{font-size:6px;color:var(--muted);line-height:1.55}
.contact-lines{margin-top:8px}
.post{margin-bottom:7px}
.post p{font-size:6px}
.post .meta{color:var(--orange);font-size:5.8px;margin-top:2px}
.field{margin-top:8px;height:16px;border:1px solid var(--line);font-size:6px;color:#999;padding:3px 5px}
.footer .btn{margin-top:6px;font-size:6.5px;padding:5px 12px;border-radius:2px}
.thumbs{display:grid;grid-template-columns:repeat(3,38px);gap:5px}
.thumbs div{height:38px;background:linear-gradient(135deg,#c9c2bb,#8c857f)}
.thumbs div:nth-child(even){background:linear-gradient(135deg,#d9d4cf,#a7a09a)}
</style>
</head>
<body>
<div class="page">

  <header class="topbar">
    <div class="brand">Podium Voice Hub</div>
    <div class="top-icons"><span></span><span></span><span></span></div>
  </header>
  <nav class="nav">
    <a href="#">ABOUT US</a><a href="#">SPEAKERS</a><a href="#">PROGRAM</a><a href="#">VENUE</a><a href="#">INDUSTRY</a><a href="#">GALLERY</a><a href="#">SPONSORS</a><a href="#">BLOG</a><a href="#">CONTACT US</a>
  </nav>

  <section class="hero">
    <div class="hero-photo" role="img" aria-label="Photo of a speaker presenting to a seated conference audience"></div>
    <div class="hero-copy">
      <div class="hero-title">PROFESSIONAL SPEAKERS</div>
      <div class="hero-sub">From Most Of The Business Sectors</div>
      <a class="btn btn-orange" href="#">LEARN MORE</a>
    </div>
    <div class="arrow left"><svg width="10" height="10" viewBox="0 0 10 10"><path d="M6.5 1.5 3 5l3.5 3.5" fill="none" stroke="#fff" stroke-width="1.8"/></svg></div>
    <div class="arrow right"><svg width="10" height="10" viewBox="0 0 10 10"><path d="M3.5 1.5 7 5 3.5 8.5" fill="none" stroke="#fff" stroke-width="1.8"/></svg></div>
    <div class="dots"><span></span><span></span><span></span></div>
  </section>

  <section class="welcome">
    <h2>Welcome To Podium Voice Hub</h2>
    <div class="welcome-rule"></div>
    <p>Podium Voice Hub is a full-service speaker bureau helping event organisers find the right voice for every stage. We represent keynote speakers, facilitators and hosts across every industry, and we work closely with you to match the message, the audience and the budget of your next conference or corporate event.</p>
    <a class="btn btn-white" href="#">Quick Online Contact Form</a>
  </section>

  <section class="intro">
    <div class="video">
      <div class="video-frame" role="img" aria-label="Video still of the bureau host speaking to camera">
        <div class="play"><svg width="14" height="14" viewBox="0 0 14 14"><path d="M4 2.5v9l7.5-4.5z" fill="#fff"/></svg></div>
        <div class="video-label">Click Here To Play</div>
      </div>
      <a class="btn btn-orange" href="#">I Want To Make Our Event A Great Success</a>
    </div>
    <div class="pitch">
      <h3>Are you looking for a Guest or Keynote Speaker - Inspiring, Entertaining, Industry Expert etc, <span class="accent">for a conference or special event?</span></h3>
      <p>Podium Voice Hub is the industry service designed to help people looking for speakers save precious time and frustration in finding the most suitable speaker for their needs. Suggestions are given by our founding conference speaker, who has presented around the country for a number of years and knows many of our professional speakers well.</p>
      <p>If you would like a hand finding great speaker options, simply send us the details of your event and the type of presenter you are looking for.</p>
      <ul class="ticks">
        <li><svg width="7" height="7" viewBox="0 0 8 8"><path d="M1 4.2 3.2 6.3 7 1.8" fill="none" stroke="#f39019" stroke-width="1.5"/></svg>Topics - Motivational, Marketing, Leadership, Sales, Health etc.</li>
        <li><svg width="7" height="7" viewBox="0 0 8 8"><path d="M1 4.2 3.2 6.3 7 1.8" fill="none" stroke="#f39019" stroke-width="1.5"/></svg>Speaker Types - Keynote, Facilitator, Host, Panel, MC etc.</li>
        <li><svg width="7" height="7" viewBox="0 0 8 8"><path d="M1 4.2 3.2 6.3 7 1.8" fill="none" stroke="#f39019" stroke-width="1.5"/></svg>Approximate Budget - $2,000, $5,000, $10,000+</li>
        <li><svg width="7" height="7" viewBox="0 0 8 8"><path d="M1 4.2 3.2 6.3 7 1.8" fill="none" stroke="#f39019" stroke-width="1.5"/></svg>Location - Sydney, Melbourne, Brisbane, Perth, Adelaide, Canberra</li>
      </ul>
      <p>And where we can, we will be happy to send you some speaker possibilities, trusted speakers known to deliver great results for your event.</p>
    </div>
  </section>

  <section class="note" role="region" aria-label="Please note">
    <h4>Please Note:</h4>
    <ul>
      <li>Any information you provide will only be used to help with your speaker request.</li>
      <li>Our team does not have any financial agreements with individual speakers we recommend; this service is offered as a value-add for clients.</li>
      <li>Our team will reply within two business days with a shortlist of speakers suited to your event.</li>
      <li>Please allow extra time for international speakers, as travel and availability can take longer to confirm.</li>
    </ul>
  </section>

  <footer class="footer">
    <div>
      <h5 class="brand-foot">Podium Voice Hub</h5>
      <p>Matching organisers with proven presenters for conferences, retreats and corporate events of every size across the country.</p>
      <p class="contact-lines">Phone: +1 (800) 555 0142<br>Address: 24 Harbourline Street, Westmead<br>Email: hello@podiumvoicehub.com.au</p>
    </div>
    <div>
      <h5>Recent Posts</h5>
      <div class="post"><p>Five ways a keynote can lift the energy of your annual conference.</p><p class="meta">July 27, 2015 / 0 comments</p></div>
      <div class="post"><p>How to brief a speaker so the message fits your audience.</p><p class="meta">July 27, 2015 / 0 comments</p></div>
      <div class="post"><p>Choosing between a facilitator and a keynote for your event.</p><p class="meta">July 27, 2015 / 0 comments</p></div>
    </div>
    <div>
      <h5>Newsletter Signup</h5>
      <p>Join our list for new speaker profiles, event tips and occasional offers.</p>
      <div class="field">Your Email Address</div>
      <a class="btn btn-orange" href="#">Subscribe</a>
    </div>
    <div>
      <h5>Gallery</h5>
      <div class="thumbs" role="img" aria-label="Gallery of event and speaker photos">
        <div></div><div></div><div></div><div></div><div></div><div></div><div></div><div></div><div></div>
      </div>
    </div>
  </footer>

</div>
</body>
</html>
```